Location services company card

Design a new business card for our location services company. I would like to have the front fairly standard with phone and email, logo, name, title etc. Back should feature text: "Location intelligence: make better decisions with maps." I would like either a location pin on the back to make it obvious that we are involved with maps. This could also have a small mud map on the back (use Vensu.com for design inspiration here).

Target Market(s)

Business and government

Industry/Entity Type

Consultant

Contact Information for Business Card

Name, title, address, phone, mobile, email

Font styles to use
Sans Serif

Requirements
Must have
• Flat design with the company colours:
• C60 M0 Y100 K0 and C100 M20 Y0 K65
• Location pin and/or mud map on back.
• Design must be similar/consistent in feel to tqav.com.au

```html
<!DOCTYPE html>
<html lang="en">
<head>
<meta charset="utf-8">
<title>TQAV – Location intelligence card back</title>
<link rel="stylesheet" href="https://fonts.googleapis.com/css2?family=Open+Sans:wght@400&display=swap">
<style>
  :root {
    --page: #ffffff;
    --navy: #01466b;
    --green: #73be44;
    --pin-hole: #ffffff;
    --headline: #ffffff;
    --brand-faint: rgba(255, 255, 255, 0.12);
  }
  html, body {
    margin: 0;
    padding: 0;
    overflow: hidden;
    background: var(--page);
  }
  .canvas {
    position: relative;
    width: 1200px;
    height: 686px;
    overflow: hidden;
    background: var(--page);
    font-family: "Open Sans", Verdana, sans-serif;
  }
  .card-back {
    position: absolute;
    left: 42px;
    top: 42px;
    width: 1118px;
    height: 602px;
    background: var(--navy);
    overflow: hidden;
  }
  .card-art {
    position: absolute;
    inset: 0;
    width: 100%;
    height: 100%;
    display: block;
  }
  .hill { fill: var(--green); }
  .pin { fill: var(--green); }
  .pin-hole { fill: var(--pin-hole); }
  .brand-name {
    position: absolute;
    left: 0;
    right: 0;
    top: 466px;
    margin: 0;
    text-align: center;
    color: var(--brand-faint);
    font-size: 104px;
    font-weight: 400;
    line-height: 1;
  }
  .headline {
    position: absolute;
    left: 75px;
    top: 411px;
    margin: 0;
    color: var(--headline);
    font-size: 36px;
    font-weight: 400;
    line-height: 1.3;
    white-space: nowrap;
  }
</style>
</head>
<body>
  <main class="canvas">
    <section class="card-back">
      <svg class="card-art" viewBox="0 0 1118 602" aria-hidden="true">
        <path class="hill" d="M0 385 Q559 137 1118 385 L1118 602 L0 602 Z"/>
        <path class="pin" d="M559 262 C546 235 506 182 506 153 A53 53 0 0 1 612 153 C612 182 572 235 559 262 Z"/>
        <circle class="pin-hole" cx="559" cy="165" r="25"/>
      </svg>
      <h1 class="headline">Location intelligence: make better decision with maps.</h1>
      <p class="brand-name">tqav</p>
    </section>
  </main>
</body>
</html>
```